RW Frameworks Inc Business cards

We need business cards using our existing logo but slightly modified. Right now the logo says RW Framework Masonry. We want to keep the RW part of the design, but replace the Framework Masonry portion with "FRAMEWORKS". Please see the attached file.
Ideally this would be a blank template so we can add Different Names, titles, and phone numbers later.
On the one side we want only the logo and on the other side the detail. I'm attaching an example for you to see.
Please reach out with any other questions. Our address and other details will be given out once we find a design we like.

Target Market(s)

Construction Industry

```html
<!DOCTYPE html>
<html lang="en">
<head>
<meta charset="UTF-8">
<title>RW Frameworks Inc – Business Cards</title>
<link href="https://fonts.googleapis.com/css2?family=Archivo:wght@400;800&family=Arimo:wght@400&display=swap" rel="stylesheet">
<style>
  :root {
    --brand-blue: #2277bb;
    --ink-grey: #7a7a7a;
    --paper: #f7f7f7;
    --backdrop: #dcdcdc;
    --rule: #c9c9c9;
  }
  * { box-sizing: border-box; margin: 0; padding: 0; }
  html, body { width: 1200px; height: 930px; overflow: hidden; }
  body {
    background: var(--backdrop);
    display: flex;
    align-items: center;
    justify-content: center;
    gap: 60px;
    font-family: "Arimo", Arial, sans-serif;
  }
  .card {
    width: 520px;
    height: 298px;
    box-shadow: 0 6px 18px rgba(0,0,0,0.12);
    position: relative;
    flex: none;
  }
  /* Detail side */
  .card--front {
    background: var(--paper);
    display: flex;
    align-items: center;
  }
  .card__brand {
    width: 262px;
    padding: 0 26px 0 30px;
    display: flex;
    justify-content: center;
    align-items: center;
    gap: 8px;
    flex: none;
  }
  .wordmark {
    font-family: "Archivo", Arial, sans-serif;
    font-weight: 800;
    letter-spacing: 1px;
    text-transform: uppercase;
    line-height: 1;
    white-space: nowrap;
  }
  .card__brand .wordmark { color: var(--brand-blue); font-size: 19px; }
  .brand-square { width: 12px; height: 12px; background: var(--brand-blue); flex: none; }
  .card__divider {
    width: 1px;
    height: 120px;
    background: var(--rule);
    flex: none;
  }
  .card__details { padding-left: 26px; }
  .person-name {
    font-family: "Archivo", Arial, sans-serif;
    font-weight: 800;
    font-size: 16px;
    letter-spacing: 1px;
    color: var(--brand-blue);
    text-transform: uppercase;
    white-space: nowrap;
  }
  .person-title { color: var(--ink-grey); font-size: 14px; margin: 3px 0 10px; }
  .contact-list { list-style: none; }
  .contact-list li {
    display: flex;
    align-items: center;
    gap: 7px;
    color: var(--ink-grey);
    font-size: 14px;
    line-height: 21px;
    white-space: nowrap;
  }
  .contact-list svg { width: 13px; height: 13px; flex: none; fill: var(--brand-blue); }
  .highlight { color: var(--brand-blue); }
  /* Logo side */
  .card--back {
    background: var(--brand-blue);
    display: flex;
    align-items: center;
    justify-content: center;
  }
  .card--back .wordmark { color: #fff; font-size: 40px; }
</style>
</head>
<body>
  <section class="card card--front" aria-label="Business card, detail side">
    <div class="card__brand">
      <span class="brand-square"></span>
      <span class="wordmark">RW Frameworks</span>
    </div>
    <div class="card__divider"></div>
    <div class="card__details">
      <p class="person-name">Daniel Hartley</p>
      <p class="person-title">Managing Director</p>
      <ul class="contact-list">
        <li>
          <svg viewBox="0 0 24 24" aria-hidden="true"><path d="M6.6 10.8a15.1 15.1 0 0 0 6.6 6.6l2.2-2.2c.3-.3.7-.4 1-.2 1.1.4 2.3.6 3.6.6.6 0 1 .4 1 1V20c0 .6-.4 1-1 1A17 17 0 0 1 3 4c0-.6.4-1 1-1h3.5c.6 0 1 .4 1 1 0 1.3.2 2.5.6 3.6.1.3 0 .7-.2 1z"/></svg>
          <span class="contact-text">044-555 010 234</span>
        </li>
        <li>
          <svg viewBox="0 0 24 24" aria-hidden="true"><path d="M2 5h20v14H2z M2 5l10 8 10-8" fill="none" stroke="#2277bb" stroke-width="2.4"/></svg>
          <span class="contact-text">info@rwframeworks.com</span>
        </li>
        <li>
          <svg viewBox="0 0 24 24" aria-hidden="true"><circle cx="12" cy="12" r="10" fill="none" stroke="#2277bb" stroke-width="2.2"/><path d="M2 12h20M12 2c3 3 3 17 0 20M12 2c-3 3-3 17 0 20" fill="none" stroke="#2277bb" stroke-width="2"/></svg>
          <span class="contact-text">www.<span class="highlight">rwframeworks</span>.com</span>
        </li>
      </ul>
    </div>
  </section>

  <section class="card card--back" aria-label="Business card, logo side">
    <span class="wordmark">RW Frameworks</span>
  </section>
</body>
</html>
```